Bramwell Business Cards

Logo files are included. Full "Bramwell" logo should be included on the back of the business card. The B symbol should be included on the front with the contact information.

Bramwell, LLC is the company name and we do commercial construction and real estate development consulting services. Look for a fairly simple card design utilizing our logo.

```html
<!DOCTYPE html>
<html lang="en">
<head>
<meta charset="utf-8">
<title>Bramwell Business Cards</title>
<link href="https://fonts.googleapis.com/css2?family=Poppins:wght@400;500;600&display=swap" rel="stylesheet">
<style>
  :root {
    --navy: #17354a;
    --navy-deep: #0f2433;
    --pattern-light: #2f6f96;
    --gold: #f0ad00;
    --white: #ffffff;
    --stage: #e9ebee;
  }
  * { box-sizing: border-box; margin: 0; padding: 0; }
  html, body { width: 1200px; height: 874px; overflow: hidden; }
  body {
    background: var(--stage);
    font-family: "Poppins", sans-serif;
    position: relative;
  }
  .card {
    position: absolute;
    left: 240px;
    width: 720px;
    height: 400px;
    overflow: hidden;
    box-shadow: 0 6px 18px rgba(0,0,0,0.18);
  }
  /* Back */
  .card-back { top: 22px; background: var(--navy); }
  .card-back .pattern-fill {
    position: absolute; inset: 0;
    background: linear-gradient(120deg, var(--pattern-light) 0%, #1f4d6b 40%, var(--navy) 70%, var(--navy-deep) 100%);
  }
  .card-back .corner-mark {
    position: absolute; right: 44px; bottom: 40px;
    width: 70px; height: 70px; border-radius: 50%;
    border: 4px solid var(--white);
  }
  /* Front */
  .card-front { top: 452px; background: var(--white); }
  .gold-band { position: absolute; top: 0; left: 0; right: 0; height: 14px; background: var(--gold); }
  .brand {
    position: absolute; top: 44px; left: 0; right: 0;
    display: flex; flex-direction: column; align-items: center; gap: 10px;
  }
  .brand-dot {
    width: 68px; height: 68px; border-radius: 50%;
    background: var(--gold);
  }
  .brand-name {
    color: var(--navy); font-weight: 500; font-size: 50px;
    letter-spacing: 3px; line-height: 1;
  }
  .info-panel {
    position: absolute; left: 0; right: 0; bottom: 0; height: 182px;
    background: var(--navy); color: var(--white);
  }
  .person { position: absolute; left: 40px; top: 26px; }
  .person-name { color: var(--gold); font-weight: 600; font-size: 24px; letter-spacing: 0.5px; line-height: 1.1; }
  .person-title { font-size: 16px; margin-bottom: 10px; }
  .person-address { font-size: 16px; line-height: 1.35; }
  .contact {
    position: absolute; right: 36px; bottom: 22px;
    list-style: none; font-size: 16px; line-height: 1.45;
  }
  .contact li { display: flex; align-items: center; justify-content: flex-end; gap: 12px; }
  .contact svg { width: 14px; height: 14px; fill: var(--gold); flex: none; }
</style>
</head>
<body>
  <section class="card card-back" aria-label="Card back">
    <div class="pattern-fill" role="img" aria-label="Repeating tone-on-tone pattern of the Bramwell B symbol"></div>
    <div class="corner-mark" aria-hidden="true"></div>
  </section>

  <section class="card card-front" aria-label="Card front">
    <div class="gold-band"></div>
    <div class="brand">
      <div class="brand-dot" aria-hidden="true"></div>
      <div class="brand-name">BRAMWELL</div>
    </div>
    <div class="info-panel">
      <div class="person">
        <p class="person-name">DANIEL FOSTER</p>
        <p class="person-title">President</p>
        <p class="person-address">4120 Alder Court<br>Juneau, Alaska 99801</p>
      </div>
      <ul class="contact">
        <li>555-014-2738
          <svg viewBox="0 0 24 24" aria-hidden="true"><path d="M6.6 10.8a15 15 0 0 0 6.6 6.6l2.2-2.2c.3-.3.7-.4 1-.2 1.1.4 2.3.6 3.6.6.6 0 1 .4 1 1V20c0 .6-.4 1-1 1A17 17 0 0 1 3 4c0-.6.4-1 1-1h3.5c.6 0 1 .4 1 1 0 1.3.2 2.5.6 3.6.1.3 0 .7-.2 1z"/></svg>
        </li>
        <li>555-017-6390
          <svg viewBox="0 0 24 24" aria-hidden="true"><path d="M7 1h10a2 2 0 0 1 2 2v18a2 2 0 0 1-2 2H7a2 2 0 0 1-2-2V3a2 2 0 0 1 2-2zm0 4v13h10V5zm5 14.5a1 1 0 1 0 0 2 1 1 0 0 0 0-2z"/></svg>
        </li>
        <li>info@bramwell.com
          <svg viewBox="0 0 24 24" aria-hidden="true"><path d="M2 5h20v14H2zm2 2v.5l8 5 8-5V7zm0 2.8V17h16V9.8l-8 5z"/></svg>
        </li>
        <li>www.bramwell.com
          <svg viewBox="0 0 24 24" aria-hidden="true"><path d="M12 2a10 10 0 1 0 0 20 10 10 0 0 0 0-20zm6.9 6h-3a15 15 0 0 0-1.3-3.9A8 8 0 0 1 18.9 8zM12 4c.8 1.2 1.5 2.5 1.9 4h-3.8c.4-1.5 1.1-2.8 1.9-4zM4.3 14a8 8 0 0 1 0-4h3.4a16 16 0 0 0 0 4zm.8 2h3a15 15 0 0 0 1.3 3.9A8 8 0 0 1 5.1 16zm3-8h-3a8 8 0 0 1 4.3-3.9A15 15 0 0 0 8.1 8zM12 20c-.8-1.2-1.5-2.5-1.9-4h3.8c-.4 1.5-1.1 2.8-1.9 4zm2.3-6H9.7a14 14 0 0 1 0-4h4.6a14 14 0 0 1 0 4zm.3 5.9a15 15 0 0 0 1.3-3.9h3a8 8 0 0 1-4.3 3.9zm1.7-5.9a16 16 0 0 0 0-4h3.4a8 8 0 0 1 0 4z"/></svg>
        </li>
      </ul>
    </div>
  </section>
</body>
</html>
```